Harbor Shell Interiors web design

We need to relaunch my commercial and retail interior design + construction company after being out of the industry's for 10 plus years.

```html
<!DOCTYPE html>
<html lang="en">
<head>
<meta charset="utf-8">
<title>Harbor Shell Interiors</title>
<link href="https://fonts.googleapis.com/css2?family=Krona+One&family=Mulish:wght@400;600;700&display=swap" rel="stylesheet">
<style>
:root{
  --blue:#1a8cff;
  --ink:#111;
  --text:#555;
  --black:#000;
  --grey:#f3f3f3;
  --line:#cfcfcf;
  --white:#fff;
}
*{margin:0;padding:0;box-sizing:border-box}
html,body{width:1200px;height:4839px;overflow:hidden;background:var(--white)}
body{position:relative;font-family:"Mulish",sans-serif;color:var(--text)}
.abs{position:absolute}
.display{font-family:"Krona One",sans-serif;color:var(--ink)}
.ph{position:absolute}
.link{position:absolute;font-size:13px;color:var(--blue);letter-spacing:.3px;display:flex;align-items:center;gap:12px;padding-bottom:6px;border-bottom:1px solid var(--blue)}
.btn{position:absolute;background:var(--blue);color:var(--white);font-size:13px;display:flex;align-items:center;justify-content:center;letter-spacing:.3px}

/* header */
.topbar{position:absolute;left:704px;top:0;width:496px;height:34px;background:var(--black);color:var(--white);font-size:14px;display:flex;align-items:center;gap:20px;padding-left:16px;white-space:nowrap}
.topbar span{display:flex;align-items:center;gap:6px}
.brand{position:absolute;display:flex;align-items:center;gap:12px}
.brand .mark{width:18px;height:18px;background:var(--blue)}
.brand .name{font-family:"Krona One",sans-serif;color:var(--ink);line-height:1.05}
.nav{position:absolute;top:56px;left:560px;display:flex;gap:38px;font-size:13px;color:var(--ink)}

/* hero */
.hero{position:absolute;left:0;top:103px;width:1200px;height:617px;clip-path:polygon(0 0,100% 0,100% 564px,50% 617px,0 564px);background:linear-gradient(160deg,#6b5a48,#3b3a38 45%,#2a2b2d)}
.hero-title{position:absolute;top:262px;left:0;width:1200px;text-align:center;color:var(--white);font-family:"Krona One",sans-serif;font-size:44px;line-height:56px}
.hero-sub{position:absolute;top:378px;width:1200px;text-align:center;color:var(--white);font-size:30px}

/* about */
.rule{position:absolute;height:1px;background:#888}
.about-p{position:absolute;left:300px;width:550px;text-align:center;font-size:12.5px;line-height:23px;color:#444}

/* services */
.services{position:absolute;top:1484px;left:0;width:1200px;height:736px;background:var(--black);overflow:hidden}
.card{position:absolute;top:197px;height:351px;border:4px solid #2a2a2a}
.card-label{position:absolute;left:18px;bottom:48px;font-family:"Krona One",sans-serif;color:var(--white);font-size:19px;line-height:26px}

/* testimonial */
.quote{position:absolute;top:3686px;width:240px;text-align:center;font-size:12.5px;line-height:24px;color:#444}
.quote b{display:block;font-family:"Krona One",sans-serif;font-size:11px;color:var(--ink);font-weight:400;margin-top:2px}

/* contact */
.contact{position:absolute;top:3919px;left:0;width:1200px;height:522px;background:linear-gradient(135deg,#1f1f20,#141414 60%,#262321)}
.field{position:absolute;border-bottom:1px solid #8a8a8a;height:48px}
.field .lbl{font-family:"Krona One",sans-serif;font-size:10px;color:var(--white)}
.field .hint{font-size:12.5px;color:#aaa;margin-top:8px}

/* footer */
.foot-h{position:absolute;top:4524px;font-family:"Krona One",sans-serif;font-size:16px;color:var(--ink)}
.foot-list{position:absolute;list-style:none;font-size:14px;color:#333}
.foot-list li{height:33px;display:flex;align-items:center;gap:10px}
.dot{width:24px;height:24px;border:1.5px solid var(--blue);border-radius:50%}
</style>
</head>
<body>

<header>
  <div class="topbar">
    <span><svg width="14" height="14" viewBox="0 0 24 24"><path fill="#1a8cff" d="M6.6 10.8a15 15 0 0 0 6.6 6.6l2.2-2.2c.3-.3.7-.4 1-.2 1.1.4 2.3.6 3.6.6.6 0 1 .4 1 1V20c0 .6-.4 1-1 1A17 17 0 0 1 3 4c0-.6.4-1 1-1h3.5c.6 0 1 .4 1 1 0 1.3.2 2.5.6 3.6.1.3 0 .7-.2 1z"/></svg>03 5550 0142</span>
    <span><svg width="15" height="12" viewBox="0 0 24 18"><rect x="1" y="1" width="22" height="16" fill="none" stroke="#1a8cff" stroke-width="2"/><path d="M1 1l11 9 11-9" fill="none" stroke="#1a8cff" stroke-width="2"/></svg>info@harborshell.example</span>
  </div>
  <div class="brand" style="left:141px;top:20px"><div class="mark"></div><div class="name" style="font-size:17px">HARBOR<br>SHELL<br>INTERIORS</div></div>
  <nav class="nav"><span>HOME</span><span>SERVICES</span><span>PORTFOLIO</span><span>CONTACT</span></nav>
  <div class="btn" style="left:945px;top:49px;width:112px;height:34px">GET A QUOTE</div>
</header>

<section class="hero" role="img" aria-label="Open-plan office with people working at desks and a leather lounge">
</section>
<h1 class="hero-title">Commercial and Retail Interior<br>Design, Fitment &amp; Construction</h1>
<p class="hero-sub">10+ Years of Experience</p>
<div class="btn" style="left:525px;top:445px;width:176px;height:34px">VIEW OUR PORTFOLIO</div>

<section class="about">
  <div class="ph" style="left:69px;top:826px;width:183px;height:222px;background:linear-gradient(160deg,#e6e6e6,#8a8f99)" role="img" aria-label="Construction workers in hard hats talking on site"></div>
  <div class="ph" style="left:890px;top:768px;width:286px;height:276px;background:linear-gradient(160deg,#f4f4f4,#c7cfd6)" role="img" aria-label="Pencil sketch of an office interior"></div>
  <div class="ph" style="left:24px;top:1121px;width:258px;height:244px;background:linear-gradient(160deg,#e9e9ea,#5b5f66)" role="img" aria-label="Two professionals reviewing plans at a desk"></div>
  <div class="ph" style="left:376px;top:1185px;width:184px;height:223px;background:linear-gradient(160deg,#d8c54a,#3c3b3a)" role="img" aria-label="Office interior with yellow feature wall"></div>
  <div class="ph" style="left:751px;top:1149px;width:378px;height:209px;background:linear-gradient(160deg,#a9b1b8,#d98a2a 70%,#5a5a5a)" role="img" aria-label="Engineers in safety vests reviewing a blueprint"></div>

  <div class="rule" style="left:351px;top:822px;width:147px"></div>
  <div class="rule" style="left:699px;top:822px;width:150px"></div>
  <div class="brand" style="left:530px;top:807px;gap:6px"><div class="mark" style="width:10px;height:10px"></div><div class="name" style="font-size:8px">HARBOR<br>SHELL<br>INTERIORS</div></div>

  <h2 class="display abs" style="top:856px;width:1200px;text-align:center;font-size:36px">About Us</h2>
  <p class="about-p" style="top:913px">At Harbor Shell Interiors, We Were Founded With Your Needs At The Forefront—a Dedication To Delivering A Transformative Leap In Results For Your Commercial And Retail Projects. Our Pride Lies In Surpassing Client Expectations, Achieved Through Meticulous Planning And Proactive Problem-solving Before Challenges Even Surface."</p>
  <p class="about-p" style="top:1016px">Guided By The Expertise Of Interior Designer And Commercial Builder, Mr. Daniel Ostrander Since 1994, Our Dedicated Team Seamlessly Manages Every Facet Of Your Project.</p>
  <p class="display abs" style="top:1074px;width:1200px;text-align:center;font-size:17px">We Work In <span style="color:var(--blue)">Australia.</span></p>
  <div class="link" style="left:537px;top:1120px">CONTACT US <svg width="20" height="10" viewBox="0 0 20 10"><path d="M0 5h18M14 1l4 4-4 4" fill="none" stroke="#1a8cff" stroke-width="1.5"/></svg></div>
</section>

<section class="services">
  <h2 class="display abs" style="left:145px;top:95px;font-size:33px;line-height:46px;color:var(--white)">Our<br>Services</h2>
  <p class="abs" style="left:370px;top:88px;width:445px;font-size:12.5px;line-height:23px;color:#ddd">It is a long established fact that a reader will be distracted by the readable content of a page when looking at its layout. The point of using Lorem Ipsum is that it has a more-or-less normal distribution of letters.</p>
  <div class="btn" style="left:847px;top:105px;width:212px;height:32px">CONTACT US FOR A QUOTE</div>

  <div class="card" style="left:141px;width:276px;background:linear-gradient(160deg,#2f7fa8,#d9d4c9 55%,#b9a98e)" role="img" aria-label="Bright open office with teal and white interior">
    <div class="card-label">INTERIOR<br>DESIGN</div>
  </div>
  <div class="card" style="left:441px;width:276px;background:linear-gradient(160deg,#cfc9bd,#c9d24a 55%,#6a4c34)" role="img" aria-label="Site workers reviewing plans by timber partitions"></div>
  <div class="card" style="left:744px;width:276px;background:linear-gradient(160deg,#e8e8e8,#b5e43a 50%,#7a3b2a)" role="img" aria-label="Worker laying bricks"></div>
  <div class="card" style="left:1044px;width:200px;background:linear-gradient(160deg,#6b6f74,#d6d0c3)" role="img" aria-label="Designers working over drawings"></div>

  <svg class="abs" style="left:308px;top:612px" width="26" height="14" viewBox="0 0 26 14"><path d="M26 7H3M8 2L3 7l5 5" fill="none" stroke="#1a8cff" stroke-width="2"/></svg>
  <svg class="abs" style="left:346px;top:588px" width="66" height="66" viewBox="0 0 66 66"><circle cx="33" cy="33" r="33" fill="#fff"/><path d="M21 33h23M38 27l6 6-6 6" fill="none" stroke="#1a8cff" stroke-width="2"/></svg>
  <div class="abs" style="left:443px;top:620px;width:442px;height:2px;background:#333"></div>
  <div class="abs" style="left:443px;top:620px;width:40px;height:2px;background:#777"></div>
</section>

<section class="expertise">
  <div class="ph" style="left:0;top:2220px;width:600px;height:516px;background:linear-gradient(160deg,#e7c7a6,#b98a62 45%,#a7b86c 75%,#6b6a64)" role="img" aria-label="Builder in hard hat reading plans at a timber-framed construction site"></div>
  <h2 class="display abs" style="left:655px;top:2326px;font-size:35px;line-height:46px">Expertise In Both<br>Design &amp;<br>Construction</h2>
  <p class="abs" style="left:655px;top:2474px;width:400px;font-size:12.5px;line-height:23px">It is a long established fact that a reader will be distracted by the readable content of a page when looking at its layout.</p>
  <p class="abs" style="left:655px;top:2532px;width:400px;font-size:12.5px;line-height:23px">It is a long established fact that a reader will be distracted by the readable content of a page when looking at its layout.</p>
  <div class="link" style="left:655px;top:2596px">CONTACT US <svg width="20" height="10" viewBox="0 0 20 10"><path d="M0 5h18M14 1l4 4-4 4" fill="none" stroke="#1a8cff" stroke-width="1.5"/></svg></div>
</section>

<section class="portfolio">
  <h2 class="display abs" style="top:2814px;width:1200px;text-align:center;font-size:36px">Our Portfolio</h2>
  <div class="ph" style="left:0;top:2892px;width:282px;height:366px;background:linear-gradient(180deg,#a9a8a4,#a8784a 30%,#9a6c40 70%,#6d7077);box-shadow:0 0 0 7px #e4e4e4" role="img" aria-label="Lounge with timber wall and white chairs"></div>
  <div class="ph" style="left:302px;top:2892px;width:284px;height:366px;background:linear-gradient(180deg,#3c3d3f,#7a7874 50%,#a58c6c);box-shadow:0 0 0 7px #e4e4e4" role="img" aria-label="Open-plan office with pendant lights"></div>
  <div class="ph" style="left:605px;top:2892px;width:285px;height:366px;background:linear-gradient(160deg,#f4f6f7,#d9dde0);box-shadow:0 0 0 7px #e4e4e4" role="img" aria-label="White minimalist reception counter"></div>
  <div class="ph" style="left:909px;top:2892px;width:282px;height:366px;background:linear-gradient(180deg,#d8dde0,#eef0f1 45%,#6aa34a 60%,#f0f0f0 75%,#bfc3c6);box-shadow:0 0 0 7px #e4e4e4" role="img" aria-label="Bright workstations with planters"></div>
  <div class="link" style="left:510px;top:3291px">VIEW MORE PROJECTS <svg width="20" height="10" viewBox="0 0 20 10"><path d="M0 5h18M14 1l4 4-4 4" fill="none" stroke="#1a8cff" stroke-width="1.5"/></svg></div>
</section>

<section class="testimonials">
  <h2 class="display abs" style="top:3396px;width:1200px;text-align:center;font-size:36px">Testimonials</h2>
  <div class="abs" style="left:0;top:3647px;width:1200px;height:124px;background:var(--grey)"></div>
  <div class="ph" style="left:189px;top:3465px;width:200px;height:182px;background:linear-gradient(180deg,#fff,#cfd3d8 40%,#26334a)" role="img" aria-label="Portrait of client Evan Castell"></div>
  <div class="ph" style="left:499px;top:3465px;width:200px;height:182px;background:linear-gradient(180deg,#fff,#d8c3b4 40%,#e0457a)" role="img" aria-label="Portrait of client Mira Delane"></div>
  <div class="ph" style="left:811px;top:3465px;width:200px;height:182px;background:linear-gradient(180deg,#fff,#e0d0c2 40%,#9aa0a8)" role="img" aria-label="Portrait of client Owen Hartley"></div>
  <svg class="abs" style="left:37px;top:3567px" width="66" height="66" viewBox="0 0 66 66"><circle cx="33" cy="33" r="32" fill="#fff" stroke="#888" stroke-width="1.5" stroke-dasharray="60 8"/><path d="M44 33H22M28 27l-6 6 6 6" fill="none" stroke="#222" stroke-width="2"/></svg>
  <svg class="abs" style="left:1096px;top:3567px" width="66" height="66" viewBox="0 0 66 66"><circle cx="33" cy="33" r="32" fill="#fff" stroke="#1a8cff" stroke-width="1.5" stroke-dasharray="60 8"/><path d="M22 33h22M38 27l6 6-6 6" fill="none" stroke="#1a8cff" stroke-width="2"/></svg>
  <p class="quote" style="left:169px">"sed diam nonummy nibh euismod tincidunt ut laoreet"<b>Evan Castell</b></p>
  <p class="quote" style="left:479px">"sed diam nonummy nibh euismod tincidunt ut laoreet"<b>Mira Delane</b></p>
  <p class="quote" style="left:791px">"sed diam nonummy nibh euismod tincidunt ut laoreet"<b>Owen Hartley</b></p>
  <div class="link" style="left:541px;top:3809px">CONTACT US <svg width="20" height="10" viewBox="0 0 20 10"><path d="M0 5h18M14 1l4 4-4 4" fill="none" stroke="#1a8cff" stroke-width="1.5"/></svg></div>
</section>

<section class="contact" role="img" aria-label="Dimly lit office interior behind the contact form"></section>
<h2 class="display abs" style="top:3995px;width:1200px;text-align:center;font-size:36px;color:var(--white)">Contact Us</h2>
<div class="field" style="left:306px;top:4076px;width:276px"><div class="lbl">FULL NAME*</div><div class="hint">Fill your full name</div></div>
<div class="field" style="left:618px;top:4076px;width:278px"><div class="lbl">COMPANY ADDRESS*</div><div class="hint">Fill your company address</div></div>
<div class="field" style="left:306px;top:4162px;width:276px"><div class="lbl">PHONE NUMBER*</div><div class="hint">Fill your phone number</div></div>
<div class="field" style="left:618px;top:4162px;width:278px"><div class="lbl">Email Address*</div><div class="hint">Fill your email address</div></div>
<div class="field" style="left:306px;top:4248px;width:590px"><div class="lbl">INQUIRES*</div><div class="hint">Fill your inquiries &amp; request</div></div>
<div class="btn" style="left:539px;top:4325px;width:122px;height:30px">GET IN TOUCH</div>

<footer>
  <h3 class="foot-h" style="left:143px">QUICK LINKS</h3>
  <ul class="foot-list" style="left:143px;top:4551px">
    <li>› Home</li><li>› Services</li><li>› Portfolio</li><li>› Contact</li><li>› Get A Quote</li>
  </ul>
  <div class="brand" style="left:454px;top:4592px"><div class="mark" style="width:22px;height:22px"></div><div class="name" style="font-size:19px">HARBOR<br>SHELL<br>INTERIORS</div></div>
  <h3 class="foot-h" style="left:926px">FOLLOW US</h3>
  <ul class="foot-list" style="left:926px;top:4558px">
    <li style="height:43px"><span class="dot"></span>Pinwheel</li>
    <li style="height:43px"><span class="dot"></span>Chirpline</li>
    <li style="height:43px"><span class="dot"></span>Workmesh</li>
    <li style="height:43px"><span class="dot"></span>Snapframe</li>
  </ul>
  <div class="abs" style="left:143px;top:4798px;width:914px;height:1px;background:var(--line)"></div>
  <p class="abs" style="top:4811px;width:1200px;text-align:center;font-size:12px;color:#333">© 2024 Harbor Shell Interiors. All Rights Reserved.</p>
</footer>

</body>
</html>
```